Redesign of Business Cards to Update them!

We want a full overhaul of our business cards! We have a design that is almost 5 years old and it needs to be updated to be current

Address is 437 Dunmore Lane Suite F Redmont Hills CA 90417
PH: 9094718263
Zorlivo.com

Hours M-F 10AM-4PM
Sat and Sunday Closed

```html
<!DOCTYPE html>
<html lang="en">
<head>
<meta charset="utf-8">
<title>Zorlivo Business Cards</title>
<link href="https://fonts.googleapis.com/css2?family=Nunito:wght@400;500;600;700;800;900&display=swap" rel="stylesheet">
<style>
  :root {
    --page: #e9e6e1;
    --ink: #111111;
    --card-black: #000000;
    --card-white: #f8f8f8;
    --brand-red: #e3232b;
    --brand-red-soft: #f4c9cb;
    --white: #ffffff;
  }
  * { margin: 0; padding: 0; box-sizing: border-box; }
  html, body { width: 900px; height: 1200px; overflow: hidden; }
  body {
    background: var(--page);
    font-family: "Nunito", sans-serif;
    color: var(--ink);
    position: relative;
  }
  .card {
    position: absolute;
    width: 773px;
    height: 448px;
    border-radius: 26px;
    overflow: hidden;
  }
  .card-front { left: 72px; top: 135px; background: var(--card-black); }
  .card-back { left: 74px; top: 624px; background: var(--card-white); }

  /* front */
  .front-wordmark {
    position: absolute;
    left: 0; right: 0; top: 140px;
    display: flex; align-items: center; justify-content: center; gap: 24px;
    color: var(--white);
    font-weight: 900;
    font-size: 116px;
    line-height: 1;
  }
  .front-wordmark .dot {
    width: 34px; height: 34px; border-radius: 50%;
    background: var(--brand-red);
    align-self: flex-start;
  }
  .front-url {
    position: absolute;
    left: 0; right: 0; top: 378px;
    text-align: center;
    color: var(--white);
    font-weight: 700;
    font-size: 31px;
    letter-spacing: 5px;
  }

  /* back */
  .back-bands { position: absolute; inset: 0; }
  .mascot-area {
    position: absolute;
    left: 44px; top: 56px;
    width: 270px; height: 120px;
    border-radius: 12px;
    background: linear-gradient(90deg, var(--brand-red-soft), #f7dfe0);
  }
  .back-wordmark {
    position: absolute;
    left: 40px; top: 188px;
    width: 290px;
    display: flex; align-items: center; justify-content: center; gap: 12px;
    font-weight: 900;
    font-size: 50px;
    line-height: 1;
    color: var(--ink);
  }
  .back-wordmark .dot {
    width: 18px; height: 18px; border-radius: 50%;
    background: var(--brand-red);
  }
  .hours {
    position: absolute;
    left: 40px; top: 294px;
    width: 288px; height: 79px;
    border: 3px solid var(--brand-red);
    border-radius: 14px;
    padding: 7px 0 0 12px;
    font-size: 22px;
    font-weight: 600;
    line-height: 32px;
  }
  .person {
    position: absolute;
    left: 403px; top: 82px;
  }
  .person-name {
    font-size: 34px;
    font-weight: 800;
    letter-spacing: 0.5px;
    line-height: 1;
  }
  .person-name .surname { color: var(--brand-red); }
  .person-role {
    margin-top: 10px;
    font-size: 24px;
    font-weight: 600;
    letter-spacing: 3px;
    line-height: 1;
  }
  .contact {
    position: absolute;
    left: 400px;
    display: flex; align-items: flex-start; gap: 18px;
    font-size: 25px;
    font-weight: 600;
    line-height: 32px;
  }
  .contact svg { flex: none; margin-top: 6px; }
  .contact-phone { top: 224px; letter-spacing: 3px; }
  .contact-web { top: 256px; letter-spacing: 3px; }
  .contact-address { top: 315px; font-size: 23px; line-height: 32px; font-weight: 500; }
</style>
</head>
<body>

<section class="card card-front">
  <div class="front-wordmark"><span>Zorlivo</span><span class="dot"></span></div>
  <div class="front-url">WWW.ZORLIVO.COM</div>
</section>

<section class="card card-back">
  <svg class="back-bands" width="773" height="448" viewBox="0 0 773 448">
    <path d="M400 0 H773 V26 H460 Q430 26 415 12 Z" fill="var(--brand-red)"/>
    <path d="M0 420 H330 Q355 420 370 448 H0 Z" fill="var(--card-black)"/>
  </svg>

  <div class="mascot-area" role="img" aria-label="Illustration of a frustrated mascot with a broken phone turning into a happy mascot with a repaired phone"></div>

  <div class="back-wordmark"><span>Zorlivo</span><span class="dot"></span></div>

  <div class="hours">Hours M-F 10AM-4PM<br>Sat and Sunday Closed</div>

  <div class="person">
    <div class="person-name">DORIAN <span class="surname">VALE</span></div>
    <div class="person-role">MANAGER</div>
  </div>

  <div class="contact contact-phone">
    <svg width="26" height="20" viewBox="0 0 26 20" aria-hidden="true">
      <path d="M2 7 Q13 -2 24 7 L21 10 L18 7 V5 H8 V7 L5 10 Z" fill="var(--brand-red)"/>
      <rect x="5" y="10" width="16" height="9" rx="2" fill="var(--brand-red)"/>
      <circle cx="13" cy="14" r="2.5" fill="var(--card-white)"/>
    </svg>
    <span>90 94 71 8263</span>
  </div>

  <div class="contact contact-web">
    <svg width="26" height="24" viewBox="0 0 24 24" aria-hidden="true" fill="none" stroke="var(--brand-red)" stroke-width="2">
      <circle cx="12" cy="12" r="10"/>
      <ellipse cx="12" cy="12" rx="4.5" ry="10"/>
      <path d="M2 12 H22 M4 6.5 H20 M4 17.5 H20"/>
    </svg>
    <span>ZORLIVO.COM</span>
  </div>

  <div class="contact contact-address">
    <svg width="26" height="28" viewBox="0 0 24 28" aria-hidden="true">
      <path d="M12 1 C6 1 2 5.5 2 11 C2 18 12 27 12 27 C12 27 22 18 22 11 C22 5.5 18 1 12 1 Z" fill="var(--brand-red)"/>
      <circle cx="12" cy="11" r="4" fill="var(--card-white)"/>
    </svg>
    <span>437 Dunmore Lane<br>Suite F Redmont Hills<br>CA 90417</span>
  </div>
</section>

</body>
</html>
```